Vintage "Greetings from Door County" Design for Wall

I are looking to recreate the vintage "Greetings from" postcard graphic from the 1940-50s. The main focus will be the saying "Greetings from Door County". Door County is a resort area in Wisconsin and we will use this graphic as a backdrop for tourist's instagram pictures. The letters of "Door County" will include things that the area is known for such as swimming, fishing, beaches, boating, biking, camping, cherry orchards, sunsets on the water etc. I have attached an actual postcard from the 50s for Door County to help you visualize the project (Picture 1). I have also attached landmarks and iconic features of Door County to include in the letters (Pictures 2-10). I want it to be more whimsical in nature with drawings to depict these landmarks as opposed to actual realistic pictures (Example 1 & 2). Please ask any questions to help clarify the project. Thanks and good luck!
Target Market(s)
Tourists
Industry/Entity Type
Retail
Colors
Designer to choose colors to be used in the design.
Look and feel

```html
<!DOCTYPE html>
<html lang="en">
<head>
<meta charset="utf-8">
<title>Greetings from Door County, Wisconsin</title>
<link rel="stylesheet" href="https://fonts.googleapis.com/css2?family=Bungee&family=Yellowtail&family=Archivo+Black&display=swap">
<style>
  :root {
    --sky-top: #b98a78;
    --sky-glow: #f2a063;
    --horizon: #f7c27e;
    --water-top: #8a8c94;
    --water-deep: #5f6d7c;
    --ink: #111111;
    --outline: #ffffff;
    --script-blue: #2fa3e6;
    --script-light: #8fd4ff;
    --script-navy: #0b2a4a;
    --state-orange: #f07b1b;
  }
  html, body {
    margin: 0;
    padding: 0;
    width: 1200px;
    height: 1029px;
    overflow: hidden;
    background: var(--sky-top);
  }
  .postcard {
    display: block;
    width: 1200px;
    height: 1029px;
  }
  .script-greeting {
    font-family: "Yellowtail", cursive;
    font-size: 132px;
  }
  .block-word {
    font-family: "Bungee", sans-serif;
  }
  .state-name {
    font-family: "Archivo Black", sans-serif;
    font-size: 104px;
  }
</style>
</head>
<body>
<svg class="postcard" viewBox="0 0 1200 1029" xmlns="http://www.w3.org/2000/svg">
  <defs>
    <linearGradient id="sky" x1="0" y1="0" x2="0" y2="1">
      <stop offset="0" stop-color="var(--sky-top)"/>
      <stop offset="0.6" stop-color="var(--sky-glow)"/>
      <stop offset="1" stop-color="var(--horizon)"/>
    </linearGradient>
    <linearGradient id="water" x1="0" y1="0" x2="0" y2="1">
      <stop offset="0" stop-color="var(--water-top)"/>
      <stop offset="1" stop-color="var(--water-deep)"/>
    </linearGradient>
    <radialGradient id="sun-path" cx="0.5" cy="0" r="0.6">
      <stop offset="0" stop-color="#f6b27a" stop-opacity="0.8"/>
      <stop offset="1" stop-color="#f6b27a" stop-opacity="0"/>
    </radialGradient>
    <linearGradient id="script-fill" x1="0" y1="0" x2="0" y2="1">
      <stop offset="0" stop-color="var(--script-light)"/>
      <stop offset="1" stop-color="var(--script-blue)"/>
    </linearGradient>

    <linearGradient id="fill-sign" gradientUnits="userSpaceOnUse" x1="0" y1="215" x2="0" y2="520">
      <stop offset="0" stop-color="#9aa08f"/><stop offset="0.5" stop-color="#c9c3b6"/><stop offset="1" stop-color="#4d5a3c"/>
    </linearGradient>
    <linearGradient id="fill-autumn" gradientUnits="userSpaceOnUse" x1="0" y1="215" x2="0" y2="520">
      <stop offset="0" stop-color="#e6962a"/><stop offset="0.55" stop-color="#c0471c"/><stop offset="1" stop-color="#6e8ccf"/>
    </linearGradient>
    <linearGradient id="fill-barn" gradientUnits="userSpaceOnUse" x1="0" y1="215" x2="0" y2="520">
      <stop offset="0" stop-color="#a8a29a"/><stop offset="0.5" stop-color="#8a3b2e"/><stop offset="1" stop-color="#5d6b44"/>
    </linearGradient>
    <linearGradient id="fill-bluff" gradientUnits="userSpaceOnUse" x1="0" y1="215" x2="0" y2="520">
      <stop offset="0" stop-color="#d7e6f2"/><stop offset="0.4" stop-color="#5d8a3a"/><stop offset="1" stop-color="#5f86b0"/>
    </linearGradient>
    <linearGradient id="fill-tower" gradientUnits="userSpaceOnUse" x1="0" y1="565" x2="0" y2="845">
      <stop offset="0" stop-color="#b9c6cf"/><stop offset="0.5" stop-color="#6b6a62"/><stop offset="1" stop-color="#3f6a34"/>
    </linearGradient>
    <linearGradient id="fill-fire" gradientUnits="userSpaceOnUse" x1="0" y1="565" x2="0" y2="845">
      <stop offset="0" stop-color="#f8c23a"/><stop offset="0.5" stop-color="#e35a14"/><stop offset="1" stop-color="#3a2416"/>
    </linearGradient>
    <linearGradient id="fill-ferry" gradientUnits="userSpaceOnUse" x1="0" y1="565" x2="0" y2="845">
      <stop offset="0" stop-color="#cfe3f0"/><stop offset="0.5" stop-color="#e9ecef"/><stop offset="1" stop-color="#34587a"/>
    </linearGradient>
    <linearGradient id="fill-garden" gradientUnits="userSpaceOnUse" x1="0" y1="565" x2="0" y2="845">
      <stop offset="0" stop-color="#8fc4e6"/><stop offset="0.45" stop-color="#5e9a2e"/><stop offset="1" stop-color="#3d6a22"/>
    </linearGradient>
    <linearGradient id="fill-cherry" gradientUnits="userSpaceOnUse" x1="0" y1="565" x2="0" y2="845">
      <stop offset="0" stop-color="#f2f2f2"/><stop offset="0.4" stop-color="#d8182a"/><stop offset="1" stop-color="#6a9a2c"/>
    </linearGradient>
    <linearGradient id="fill-lighthouse" gradientUnits="userSpaceOnUse" x1="0" y1="565" x2="0" y2="845">
      <stop offset="0" stop-color="#9ccbe8"/><stop offset="0.55" stop-color="#f4f4f0"/><stop offset="1" stop-color="#b2342c"/>
    </linearGradient>

    <text id="door-shape" class="block-word" x="240" y="520" font-size="410" textLength="752" lengthAdjust="spacingAndGlyphs">DOOR</text>
    <text id="county-shape" class="block-word" x="36" y="845" font-size="370" textLength="1080" lengthAdjust="spacingAndGlyphs">COUNTY</text>
  </defs>

  <g class="backdrop" role="img" aria-label="Sunset sky over calm lake water">
    <rect class="sky" x="0" y="0" width="1200" height="572" fill="url(#sky)"/>
    <rect class="lake" x="0" y="572" width="1200" height="457" fill="url(#water)"/>
    <rect class="sun-reflection" x="300" y="572" width="600" height="457" fill="url(#sun-path)"/>
  </g>

  <g class="greeting">
    <text class="script-greeting" x="96" y="128" fill="none" stroke="var(--outline)" stroke-width="14" stroke-linejoin="round">Greetings from</text>
    <text class="script-greeting" x="96" y="128" fill="url(#script-fill)" stroke="var(--script-navy)" stroke-width="5" stroke-linejoin="round" paint-order="stroke">Greetings from</text>
  </g>

  <g class="headline headline-door" role="img" aria-label="DOOR in block letters filled with scenes: drive-in theatre sign, autumn road, stone barn, wooded bluff over the bay">
    <g class="extrusion" fill="var(--ink)">
      <use href="#door-shape" x="-4" y="4"/>
      <use href="#door-shape" x="-8" y="8"/>
      <use href="#door-shape" x="-12" y="12"/>
      <use href="#door-shape" x="-16" y="16"/>
    </g>
    <use class="outline" href="#door-shape" fill="none" stroke="var(--outline)" stroke-width="16" stroke-linejoin="round"/>
    <use class="outline-inner" href="#door-shape" fill="none" stroke="var(--ink)" stroke-width="6" stroke-linejoin="round"/>
    <text class="block-word" x="240" y="520" font-size="410" textLength="752" lengthAdjust="spacingAndGlyphs"><tspan fill="url(#fill-sign)">D</tspan><tspan fill="url(#fill-autumn)">O</tspan><tspan fill="url(#fill-barn)">O</tspan><tspan fill="url(#fill-bluff)">R</tspan></text>
  </g>

  <g class="headline headline-county" role="img" aria-label="COUNTY in block letters filled with scenes: lookout tower, campfire, car ferry, park lawn, cherries, lighthouse">
    <g class="extrusion" fill="var(--ink)">
      <use href="#county-shape" x="-4" y="4"/>
      <use href="#county-shape" x="-8" y="8"/>
      <use href="#county-shape" x="-12" y="12"/>
      <use href="#county-shape" x="-16" y="16"/>
    </g>
    <use class="outline" href="#county-shape" fill="none" stroke="var(--outline)" stroke-width="16" stroke-linejoin="round"/>
    <use class="outline-inner" href="#county-shape" fill="none" stroke="var(--ink)" stroke-width="6" stroke-linejoin="round"/>
    <text class="block-word" x="36" y="845" font-size="370" textLength="1080" lengthAdjust="spacingAndGlyphs"><tspan fill="url(#fill-tower)">C</tspan><tspan fill="url(#fill-fire)">O</tspan><tspan fill="url(#fill-ferry)">U</tspan><tspan fill="url(#fill-garden)">N</tspan><tspan fill="url(#fill-cherry)">T</tspan><tspan fill="url(#fill-lighthouse)">Y</tspan></text>
  </g>

  <g class="state">
    <text class="state-name" x="668" y="972" textLength="500" lengthAdjust="spacingAndGlyphs" fill="var(--ink)" transform="translate(-5 5)">WISCONSIN</text>
    <text class="state-name" x="668" y="972" textLength="500" lengthAdjust="spacingAndGlyphs" fill="var(--state-orange)" stroke="var(--ink)" stroke-width="5" stroke-linejoin="round" paint-order="stroke">WISCONSIN</text>
  </g>
</svg>
</body>
</html>
```